NEW YORK Plumbing/utility company 10 year anniversary business card

Looking For simple back and front business card would like to include a few things in description
We offer 24/7 emergency service
residential
commercial
industrial
municipal
services offered
Plumbing
hydro excavation
hydro jetting
Well pumps
Sewer pumps
water mains
sewer mains

```html
<!DOCTYPE html>
<html lang="en">
<head>
<meta charset="utf-8">
<title>Ridgeline Water &amp; Sewer – Business Card</title>
<link rel="stylesheet" href="https://fonts.googleapis.com/css2?family=Montserrat:wght@600;700;800&family=Lexend:wght@300;400&display=swap">
<style>
  :root {
    --sky: #3bb2e4;
    --slate: #9a9a9a;
    --slate-dark: #8a8a8a;
    --paper: #f6f7f8;
    --signal: #e3141b;
    --backdrop: #e9eaec;
    --white: #ffffff;
  }
  * { box-sizing: border-box; margin: 0; padding: 0; }
  html, body { width: 1200px; height: 800px; overflow: hidden; }
  body {
    background: var(--backdrop);
    display: flex;
    align-items: center;
    justify-content: center;
    gap: 40px;
    font-family: "Lexend", sans-serif;
  }
  .card {
    width: 540px;
    height: 309px;
    position: relative;
    overflow: hidden;
    box-shadow: 0 4px 14px rgba(0,0,0,.12);
  }

  /* Front */
  .card-front { display: flex; background: var(--paper); }
  .front-identity {
    width: 46%;
    padding: 34px 18px 24px 22px;
    display: flex;
    flex-direction: column;
  }
  .brand {
    display: flex;
    align-items: center;
    gap: 8px;
    font-family: "Montserrat", sans-serif;
    font-weight: 800;
    font-size: 34px;
    letter-spacing: 0.5px;
    color: var(--slate);
  }
  .brand-dot { width: 14px; height: 14px; border-radius: 50%; background: var(--sky); flex: none; }
  .region {
    margin-top: 14px;
    font-family: "Montserrat", sans-serif;
    font-weight: 700;
    font-size: 19px;
    letter-spacing: 2.5px;
    color: var(--signal);
    white-space: nowrap;
  }
  .trade {
    margin-top: 4px;
    display: flex;
    align-items: center;
    gap: 8px;
    font-family: "Montserrat", sans-serif;
    font-weight: 700;
    font-size: 13px;
    letter-spacing: 2px;
    color: var(--sky);
    white-space: nowrap;
  }
  .trade::before, .trade::after { content: ""; height: 2px; width: 26px; background: var(--sky); }
  .contact {
    margin-top: auto;
    font-size: 13px;
    letter-spacing: 1.6px;
    color: var(--signal);
    line-height: 1.45;
  }
  .front-offer {
    flex: 1;
    background: var(--sky);
    color: var(--white);
    padding: 20px 16px 16px 18px;
    font-size: 12.5px;
    line-height: 1.4;
  }
  .offer-lead { font-weight: 300; }
  .offer-list { list-style: none; padding-left: 62px; margin-top: 2px; }
  .offer-list li::before { content: "·"; margin-right: 3px; }
  .services-heading {
    margin-top: 10px;
    font-size: 11.5px;
    letter-spacing: 3px;
  }

  /* Back */
  .card-back { background: var(--slate); }
  .back-art { position: absolute; inset: 0; }
  .anniversary {
    position: absolute;
    top: 30px;
    left: 0; right: 0;
    text-align: center;
    font-weight: 300;
    font-size: 21px;
    letter-spacing: 8px;
    color: var(--paper);
  }
  .back-band {
    position: absolute;
    top: 104px;
    left: 0; right: 0;
    height: 102px;
    background: var(--paper);
    display: flex;
    align-items: center;
    justify-content: center;
    gap: 10px;
  }
  .back-band .brand { font-size: 46px; }
  .back-band .brand-dot { width: 18px; height: 18px; }
</style>
</head>
<body>

  <section class="card card-front" aria-label="Card front">
    <div class="front-identity">
      <div class="brand"><span class="brand-dot"></span>RIDGELINE</div>
      <div class="region">RIDGELINE</div>
      <div class="trade">WATER &amp; SEWER</div>
      <p class="contact">Phone: 845-555-0142<br>eMail: info@ridgelinewater.com</p>
    </div>
    <div class="front-offer">
      <p class="offer-lead">We offer 24/7 emergency service</p>
      <ul class="offer-list">
        <li>Residential</li>
        <li>Commercial</li>
        <li>Industrial</li>
        <li>Municipal</li>
      </ul>
      <p class="services-heading">SERVICES</p>
      <ul class="offer-list">
        <li>Plumbing</li>
        <li>Hydro Excavation</li>
        <li>Hydro Jetting</li>
        <li>Well Pumps</li>
        <li>Sewer Pumps</li>
        <li>Water Mains</li>
        <li>Sewer Mains</li>
      </ul>
    </div>
  </section>

  <section class="card card-back" aria-label="Card back">
    <svg class="back-art" viewBox="0 0 540 309" aria-hidden="true">
      <polygon points="0,0 70,0 0,60" fill="#3bb2e4"/>
      <polygon points="540,0 540,90 470,0" fill="#3bb2e4"/>
      <polygon points="0,309 0,240 80,309" fill="#3bb2e4"/>
      <polygon points="540,309 540,220 455,309" fill="#3bb2e4"/>
      <rect x="40" y="88" width="28" height="16" fill="#3bb2e4"/>
      <rect x="470" y="206" width="28" height="16" fill="#3bb2e4"/>
      <path d="M330,206 h70 l14,14 v40 l-14,14 h-70 z" fill="#3bb2e4"/>
      <path d="M150,104 h-30 l-14,-14 v-10 h44 z" fill="#3bb2e4"/>
    </svg>
    <p class="anniversary">10 YEAR ANNIVERSARY</p>
    <div class="back-band">
      <div class="brand"><span class="brand-dot"></span>RIDGELINE</div>
    </div>
  </section>

</body>
</html>
```